Schlichtes Website-Design für Mineralwasser
Zielgruppe
TILMO ist eine neue hochwertige Mineralwassermarke, die online bestellt werden kann. Der Stil von TILMO ist geradlinig, futuristisch, skandinavisch, minimalistisch und eher kühl. Der Markenname TILMO ist von dem lateinischen „aer“ abgeleitet und steht für das Wort „Luft“. Das Attribut „luftig-leicht“ soll daher auch im Design der Webseite wiederzufinden sein.
Die Zielgruppe für TILMO ist breit gefächert und umfasst nicht nur Privatpersonen (Studenten, Berufstätige, Familien, Singlehaushalte, ältere Personen u. a. m.) sondern auch Gewerbe, die sich Mineralwasser ins Büro liefern lassen wollen.
Aufgabenstellung
1. Es soll ein Design für die Webseite von TILMO erstellt werden, die denselben Aufbau wie die Webseite moos-perle.de hat, aber an die Wassermarke TILMO angepasst wird. Hier ist bereits die Richtung des Website-Designs mit verschiedenen Elementen, die den Screen ausfüllen, schön dargestellt.
2. Bisher ist von der Marke TILMO nur das Flaschenetikett vorhanden. Das Design der Webseite soll sich daran orientieren.
3. Das Design soll so gestaltet sein, dass in der Entwicklung eine responsive Webseite gut möglich ist. Das Design an sich soll nur für die Desktopansicht gestaltet werden.
4. Gerne kann an kleine Animationen gedacht werden, die bei der Entwicklung der Seite mit eingebaut werden können, um die Seite aufzulockern.

```html
<!DOCTYPE html>
<html lang="de">
<head>
<meta charset="utf-8">
<title>TILMO Mineralwasser</title>
<link href="https://fonts.googleapis.com/css2?family=Marcellus&family=Open+Sans:wght@400;600&display=swap" rel="stylesheet">
<style>
:root{
  --navy:#2d2b8f;
  --leise:#3c9ee2;
  --still:#e23b3b;
  --text:#8a8a8a;
  --outer:#e4e4e4;
  --page:#ffffff;
  --line:#d6d6d6;
  --haze:#ececee;
}
*{box-sizing:border-box;margin:0;padding:0}
html,body{width:1200px;height:2700px;overflow:hidden;background:var(--outer)}
.canvas{position:relative;width:1200px;height:2700px;overflow:hidden;
  background:linear-gradient(90deg,#dcdcdc 0,#ececec 82px,#fff 82px,#fff 1118px,#ececec 1118px,#dcdcdc 1200px);
  font-family:"Open Sans",Arial,sans-serif;color:var(--text)}
.abs{position:absolute}
.haze{position:absolute;left:82px;width:1036px}
.haze.top{top:0;height:135px;background:radial-gradient(ellipse 60% 70% at 25% 10%,var(--haze),rgba(255,255,255,0) 70%),radial-gradient(ellipse 40% 80% at 95% 40%,var(--haze),rgba(255,255,255,0) 70%)}
.haze.bottom{top:2600px;height:100px;background:radial-gradient(ellipse 45% 90% at 12% 80%,var(--haze),rgba(255,255,255,0) 70%),radial-gradient(ellipse 45% 90% at 90% 100%,var(--haze),rgba(255,255,255,0) 70%)}
.brand{left:0;width:1200px;top:14px;text-align:center;font-family:"Marcellus",serif;font-size:40px;letter-spacing:6px;color:var(--navy)}
.bottle{position:absolute;border-radius:40% 40% 14px 14px / 18% 18% 14px 14px}
.bottle.blur{filter:blur(3px);opacity:.75}
.slogan{left:0;width:1200px;top:442px;text-align:center;font-family:"Marcellus",serif;font-size:22px;color:var(--navy)}
.intro{left:330px;width:540px;top:471px;text-align:center;font-size:7.5px;line-height:12px;color:var(--text)}
.mouse{position:absolute;width:14px;height:22px;border:1.5px solid #b5b5b5;border-radius:7px}
.mouse::after{content:"";position:absolute;left:5px;top:4px;width:2px;height:5px;background:#b5b5b5;border-radius:1px}
.dotnav{position:absolute;left:1099px;width:8px}
.dotnav span{display:block;width:4px;height:4px;margin:0 auto 4px;border-radius:50%;background:#bcbcbc}
.dotnav span.on{width:8px;height:8px;background:var(--navy);box-shadow:0 0 0 2px #fff,0 0 0 3px var(--navy)}
.product h2{font-family:"Marcellus",serif;font-weight:400;font-size:27px;color:var(--navy);letter-spacing:.3px;white-space:nowrap}
.product p{font-size:9px;line-height:18px;margin-top:14px}
.product.right{text-align:right}
.btn{display:inline-block;margin-top:20px;width:137px;height:19px;border:1.5px solid currentColor;border-radius:3px;
  font-family:"Marcellus",serif;font-size:9px;letter-spacing:3px;line-height:16px;text-align:center}
.laut .accent{color:var(--navy)} .laut .btn{color:var(--navy)}
.leise h2 .accent{color:var(--leise)} .leise .btn{color:var(--leise)}
.still h2 .accent{color:var(--still)} .still .btn{color:var(--still)}
.deco{position:absolute}
.mineral-bg{left:0;width:1200px;top:2255px;text-align:center;font-family:"Marcellus",serif;font-size:170px;line-height:190px;letter-spacing:18px;color:#f4f4f6}
.mineral-title{left:0;width:1200px;top:2292px;text-align:center;font-family:"Marcellus",serif;font-size:21px;line-height:24px;color:var(--navy)}
.table{position:absolute;top:2389px;width:190px;font-size:9px;color:var(--navy)}
.table h3{font-family:"Marcellus",serif;font-weight:400;font-size:11px;margin-bottom:12px}
.table .row{display:flex;justify-content:space-between;height:24.7px;font-weight:600}
.table .row b{font-weight:400;color:var(--text)}
.divider{left:599px;top:2392px;width:1px;height:110px;background:var(--line)}
.footer{top:2676px;font-size:6px;color:var(--text)}
.impressum{top:2674px;left:851px;font-size:8px;color:var(--navy)}
</style>
</head>
<body>
<div class="canvas">

  <div class="haze top" role="img" aria-label="Feines Wellenlinien-Ornament in Hellgrau"></div>

  <div class="abs brand">TILMO</div>

  <div class="bottle blur" role="img" aria-label="Flasche TILMO Still, unscharf im Hintergrund" style="left:440px;top:104px;width:92px;height:310px;background:linear-gradient(180deg,#f0595b 0 8%,#eef0f3 8%,#dfe3e8 60%,#f3f5f7)"></div>
  <div class="bottle" role="img" aria-label="Glasflasche TILMO Laut mit blauem Deckel" style="left:552px;top:96px;width:98px;height:328px;background:linear-gradient(180deg,#3b5fd6 0 9%,#f4f6f9 9%,#e1e6ec 55%,#f7f8fa)"></div>
  <div class="bottle blur" role="img" aria-label="Flasche TILMO Leise, unscharf im Hintergrund" style="left:668px;top:104px;width:92px;height:310px;background:linear-gradient(180deg,#7aa7ef 0 8%,#eef0f3 8%,#dfe3e8 60%,#f3f5f7)"></div>

  <div class="abs slogan">SLOGAN&nbsp; HEADER TEXT WILL GO HERE</div>
  <div class="abs intro">Purer Geschmack trifft klares Design. Die schlichte Eleganz reduziert TILMO auf den Inhalt: reines Wasser. Frisch von der Quelle spiegelt TILMO Wasser eine bewusste Lebensweise wider. Laut, leise, still … TILMO Wasser überzeugt mit seinen drei Charakteren</div>
  <div class="mouse" style="left:593px;top:506px"></div>

  <div class="dotnav" style="top:245px"><span class="on"></span><span></span><span></span><span></span></div>
  <div class="dotnav" style="top:790px"><span class="on"></span><span></span><span></span></div>
  <div class="dotnav" style="top:1332px"><span></span><span class="on"></span><span></span></div>
  <div class="dotnav" style="top:1870px"><span></span><span></span><span class="on"></span></div>
  <div class="dotnav" style="top:2360px"><span></span><span></span><span></span><span></span><span class="on"></span></div>

  <div class="deco" role="img" aria-label="Luftblasen und Wellenlinien in Blau" style="left:755px;top:629px;width:178px;height:420px;background:radial-gradient(ellipse at 45% 35%,rgba(120,150,240,.35),rgba(170,190,250,.15) 45%,rgba(255,255,255,0) 72%)"></div>
  <div class="bottle" role="img" aria-label="PET-Flasche TILMO Laut" style="left:522px;top:566px;width:140px;height:482px;background:linear-gradient(180deg,#3d5ad8 0 9%,#eef1f5 9%,#dfe4ea 50%,#f0f3f6)"></div>
  <div class="bottle" role="img" aria-label="Glasflasche TILMO Laut" style="left:640px;top:618px;width:125px;height:434px;background:linear-gradient(180deg,#3d5ad8 0 8%,#f3f5f8 8%,#e2e6ec 55%,#f6f7f9)"></div>
  <div class="abs product right laut" style="left:299px;top:722px;width:190px">
    <h2>TILMO <span class="accent">LAUT</span></h2>
    <p>TILMO Laut ist herrlich sprudelnd sowie reich an Mineralstoffen. Das natürliche Mine&shy;ralwasser ist erfrischend und rein im Gesch&shy;mack. TILMO Laut ist die richtige Wahl für alle, die Mineralwasser am liebsten prickelnd mögen.</p>
    <span class="btn">JETZ BESTELLEN</span>
  </div>

  <div class="deco" role="img" aria-label="Luftblasen und Wellenlinien in Hellblau" style="left:262px;top:1195px;width:199px;height:377px;background:radial-gradient(ellipse at 55% 45%,rgba(90,175,235,.35),rgba(150,205,245,.15) 45%,rgba(255,255,255,0) 72%)"></div>
  <div class="bottle" role="img" aria-label="PET-Flasche TILMO Leise" style="left:522px;top:1100px;width:140px;height:480px;background:linear-gradient(180deg,#5d9fea 0 9%,#eef1f5 9%,#dfe4ea 50%,#f0f3f6)"></div>
  <div class="bottle" role="img" aria-label="Glasflasche TILMO Leise" style="left:430px;top:1154px;width:125px;height:434px;background:linear-gradient(180deg,#5d9fea 0 8%,#f3f5f8 8%,#e2e6ec 55%,#f6f7f9)"></div>
  <div class="abs product leise" style="left:711px;top:1264px;width:186px">
    <h2>TILMO <span class="accent">LEISE</span></h2>
    <p>Für alle, die es gerne ein wenig ruhiger haben, bietet TILMO Leise eine belebend sanfte Erfrischung.<br>Durch die milde Kohlensäure ist das Wasser natürlich zurückhaltend und fein perlend im Geschmack.</p>
    <span class="btn">JETZ BESTELLEN</span>
  </div>

  <div class="deco" role="img" aria-label="Wasserspritzer und Tropfen in Rot" style="left:723px;top:1708px;width:210px;height:420px;background:radial-gradient(ellipse at 40% 45%,rgba(235,110,110,.32),rgba(245,170,170,.14) 45%,rgba(255,255,255,0) 72%)"></div>
  <div class="bottle" role="img" aria-label="PET-Flasche TILMO Still" style="left:522px;top:1649px;width:140px;height:482px;background:linear-gradient(180deg,#e8543a 0 9%,#eef1f5 9%,#dfe4ea 50%,#f0f3f6)"></div>
  <div class="bottle" role="img" aria-label="Glasflasche TILMO Still" style="left:640px;top:1702px;width:125px;height:434px;background:linear-gradient(180deg,#e53a3a 0 8%,#f3f5f8 8%,#e2e6ec 55%,#f6f7f9)"></div>
  <div class="abs product right still" style="left:309px;top:1805px;width:180px">
    <h2>TILMO <span class="accent">STILL</span></h2>
    <p>TILMO Still belebt auf sanfte und natürliche Art. Wer ein Wasser ohne Kohlensäure genießen will und den natürlichen Geschmack von Wasser mag, greift zu TILMO Still.</p>
    <span class="btn">JETZ BESTELLEN</span>
  </div>

  <div class="abs mineral-bg" aria-hidden="true">TILMO</div>
  <div class="abs mineral-title">NATÜRLICHES MINERALWASSER<br>MIT KOHLENSÄURE VERSETZT</div>
  <div class="table" style="left:386px">
    <h3>KATIONEN IN MG/L</h3>
    <div class="row">NATRIUM:<b>19,0</b></div>
    <div class="row">CALCIUM:<b>110,2</b></div>
    <div class="row">MAGNESIUM:<b>5,9</b></div>
    <div class="row">KALIUM:<b>1,28</b></div>
  </div>
  <div class="abs divider"></div>
  <div class="table" style="left:634px">
    <h3>ANIONEN IN MG/L</h3>
    <div class="row">CHLORID:<b>42,0</b></div>
    <div class="row">FLUORID:<b>0,08</b></div>
    <div class="row">SULFAT:<b>73,0</b></div>
    <div class="row">HYDROGENCARBONAT:<b>240,0</b></div>
  </div>

  <div class="haze bottom" role="img" aria-label="Feines Wellenlinien-Ornament in Hellgrau"></div>
  <div class="mouse" style="left:593px;top:2645px"></div>
  <div class="abs footer" style="left:301px">Quellhaus Getränke GmbH &nbsp;|&nbsp; 20457 Nordhafen &nbsp;|&nbsp; All Right Reserved</div>
  <div class="abs impressum">IMPRESSUM</div>

</div>
</body>
</html>
```